Quellmar Aus Business card revamp

We are looking to revamp our business card design. We are hoping to change our colours to dark navey blue, gray, white and black but are open to keeping the same if a good design is submited. We are after somthing a bit differnt not just boring business card. I have attached a copy of our current card. We Want to keep the same logo design which i have attached a few to hopfully help you in this process. We are after a design that can be personalized to separate 4 people

Industry/Entity Type

Business

Colors
0455a3
ffffff
000000
cbcbcb

Requirements
Must have
• Quellmar Logo, address 3/41 Wattlebend Street, Kelvanby 4517, phone number, Name and position

```html
<!DOCTYPE html>
<html lang="en">
<head>
<meta charset="utf-8">
<title>Quellmar Aus Business Card</title>
<link href="https://fonts.googleapis.com/css2?family=Archivo+Black&family=Roboto+Condensed:ital,wght@0,400;1,400&family=Roboto:wght@400;700&display=swap" rel="stylesheet">
<style>
  :root{
    --navy:#062b52;
    --blue:#1f7fd1;
    --orange:#f06a1f;
    --orange-deep:#e2451f;
    --white:#ffffff;
    --paper:#f5f6f7;
    --grey:#cbcbcb;
    --ink-grey:#8a8a8a;
    --stage:#5c5c5c;
  }
  *{margin:0;padding:0;box-sizing:border-box}
  html,body{width:1200px;height:1200px;overflow:hidden;background:var(--stage)}
  .sheet{position:relative;width:1200px;height:1200px}
  .card{position:absolute;left:150px;width:900px;height:535px;border-radius:22px;overflow:hidden;background:var(--navy)}
  .card--front{top:38px}
  .card--back{top:627px}
  .card__waves{position:absolute;inset:0;width:900px;height:535px}

  .brand{position:absolute;left:70px;top:58px;display:flex;align-items:center;gap:14px}
  .brand__dot{width:46px;height:46px;border-radius:50%;background:var(--blue)}
  .brand__name{font-family:"Archivo Black",sans-serif;font-size:58px;line-height:1;color:var(--blue);letter-spacing:-1px}
  .brand__tagline{position:absolute;left:130px;top:124px;font-family:"Archivo Black",sans-serif;font-size:21px;color:var(--blue)}
  .abn{position:absolute;left:440px;top:162px;font-family:"Roboto Condensed",sans-serif;font-size:17px;color:var(--ink-grey)}

  .person{position:absolute;right:578px;top:384px;text-align:right;white-space:nowrap}
  .person__name{font-family:"Archivo Black",sans-serif;font-size:32px;line-height:1;color:var(--orange)}
  .person__role{font-family:"Roboto",sans-serif;font-size:19px;line-height:1;color:var(--white);margin-top:6px}

  .contacts{position:absolute;left:352px;top:388px;font-family:"Roboto Condensed",sans-serif;font-size:21px;color:var(--white);line-height:24px;white-space:nowrap}
  .contacts__row{display:flex;gap:24px;margin-bottom:15px}
  .contact{display:flex;align-items:center;gap:9px}
  .contact svg{width:22px;height:22px;flex:none}

  .back__brand{position:absolute;left:0;right:0;top:150px;display:flex;justify-content:center;align-items:center;gap:18px}
  .back__brand .brand__dot{width:70px;height:70px}
  .back__brand .brand__name{font-size:86px}
  .back__motto{position:absolute;left:0;right:0;top:362px;text-align:center;font-family:"Roboto Condensed",sans-serif;font-style:italic;font-size:29px;color:var(--orange)}
  .back__services{position:absolute;left:0;right:0;top:412px;text-align:center;font-family:"Roboto",sans-serif;font-size:21px;line-height:26px;color:var(--white)}
  .back__web{position:absolute;left:0;right:0;top:470px;text-align:center;font-family:"Roboto",sans-serif;font-weight:700;font-size:33px;color:var(--blue)}
</style>
</head>
<body>
<main class="sheet">

  <section class="card card--front" aria-label="Business card front">
    <svg class="card__waves" viewBox="0 0 900 535" aria-hidden="true">
      <defs>
        <linearGradient id="stripe" x1="0" x2="1" y1="0" y2="0">
          <stop offset="0" stop-color="#f28a1e"/>
          <stop offset="1" stop-color="#e2451f"/>
        </linearGradient>
      </defs>
      <path d="M0 0H900V292C760 330 560 350 380 300C230 258 110 236 0 212Z" fill="#cbcbcb"/>
      <path d="M0 0H900V280C760 318 560 338 380 288C230 246 110 224 0 200Z" fill="#f5f6f7"/>
      <path d="M0 137C170 170 320 250 480 282C620 308 760 290 900 248" fill="none" stroke="url(#stripe)" stroke-width="9"/>
    </svg>

    <div class="brand">
      <span class="brand__dot"></span>
      <span class="brand__name">Quellmar</span>
    </div>
    <div class="brand__tagline">Passive Fire Protection</div>
    <div class="abn">ABN: 52 184 930 276</div>

    <div class="person">
      <div class="person__name">Name Here</div>
      <div class="person__role">POSITION</div>
    </div>

    <div class="contacts">
      <div class="contacts__row">
        <span class="contact">
          <svg viewBox="0 0 24 24"><circle cx="12" cy="12" r="12" fill="#fff"/><rect x="8.5" y="5.5" width="7" height="13" rx="1.5" fill="none" stroke="#062b52" stroke-width="1.8"/><circle cx="12" cy="16" r="1" fill="#062b52"/></svg>
          545 318 2207
        </span>
        <span class="contact">
          <svg viewBox="0 0 24 24"><circle cx="12" cy="12" r="12" fill="#fff"/><path d="M9 6.5l2 3-1.4 1.4c.6 1.4 1.9 2.7 3.3 3.3l1.4-1.4 3 2-1.3 2.2c-4.6-.4-8.4-4.2-8.8-8.8Z" fill="#062b52"/></svg>
          545 318 2207
        </span>
      </div>
      <div class="contacts__row">
        <span class="contact">
          <svg viewBox="0 0 24 24"><circle cx="12" cy="12" r="12" fill="#fff"/><rect x="6" y="8" width="12" height="9" rx="1" fill="#062b52"/><path d="M6.5 8.8L12 13l5.5-4.2" fill="none" stroke="#fff" stroke-width="1.3"/></svg>
          name@quellmar.com.au
        </span>
        <span class="contact">
          <svg viewBox="0 0 24 24"><circle cx="12" cy="12" r="12" fill="#fff"/><path d="M10.5 13.5l3-3M9.2 12.2l-1.4 1.4a2 2 0 0 0 2.8 2.8l1.4-1.4M14.8 11.8l1.4-1.4a2 2 0 0 0-2.8-2.8l-1.4 1.4" fill="none" stroke="#062b52" stroke-width="1.6" stroke-linecap="round"/></svg>
          www.quellmar.com.au
        </span>
      </div>
      <div class="contacts__row">
        <span class="contact">
          <svg viewBox="0 0 24 24"><circle cx="12" cy="12" r="12" fill="#fff"/><path d="M12 5.5a4.5 4.5 0 0 0-4.5 4.5c0 3.3 4.5 8.5 4.5 8.5s4.5-5.2 4.5-8.5A4.5 4.5 0 0 0 12 5.5Z" fill="#062b52"/><circle cx="12" cy="10" r="1.7" fill="#fff"/></svg>
          3/41 Wattlebend Street, Kelvanby 4517 Queensland
        </span>
      </div>
    </div>
  </section>

  <section class="card card--back" aria-label="Business card back">
    <div class="back__brand">
      <span class="brand__dot"></span>
      <span class="brand__name">Quellmar</span>
    </div>
    <p class="back__motto">Reliability with Dedication to Service</p>
    <p class="back__services">New Installations | Fire Upgrade Works | Inspection &amp; Certification<br>Duct &amp; Steel Protection | Consultancy | Training &amp; Education</p>
    <p class="back__web">www.quellmar.com.au</p>
  </section>

</main>
</body>
</html>
```